New Business Card Design Project

Vorin focus is KLM Asset Management and Supply Chain.
We have Business Process Experts that can help you get the maximum potential out of your KLM T/7RIVA ERP. We look to understand your business and through the People, Process and Technologies to make you streamline your users digital experience.

The back of the card will be either;
- all black with the orange logo
- all orange with the black logo
- all white with the orange logo
- or make something special
The detail side, show me your best designs.
Try having the side a different colour. So if the one side is black the other is white…

Target Market(s)

Corporate Professional Business

Industry/Entity Type

Mining, Software

Contact Information for Business Card

Name, Position, brief what we do

Colors
F0912C
F2A743
F7CA91
FBE8D2
FDF5EE

Requirements
Must have
• Real Simple Solutions to Big Problems

```html
<!DOCTYPE html>
<html lang="en">
<head>
<meta charset="utf-8">
<title>Vorin Business Card</title>
<link rel="stylesheet" href="https://fonts.googleapis.com/css2?family=Cinzel:wght@400;500&family=Poppins:wght@400;500;600;700&display=swap">
<style>
  :root {
    --orange: #f47524;
    --black: #000000;
    --white: #ffffff;
    --ink: #111111;
    --backdrop: #2a2a2a;
    --rule: #3a3a3a;
  }
  * { box-sizing: border-box; margin: 0; padding: 0; }
  html, body {
    width: 1200px; height: 880px; overflow: hidden;
    background: var(--backdrop);
  }
  .canvas {
    width: 1200px; height: 880px;
    display: flex; flex-direction: column; align-items: center; justify-content: center;
    gap: 40px;
  }
  .card {
    position: relative;
    width: 700px; height: 400px;
    border-radius: 22px;
    overflow: hidden;
  }
  /* Back side */
  .card-back { background: var(--black); }
  .back-brand {
    position: absolute; left: 0; right: 0; top: 100px;
    display: flex; align-items: center; justify-content: center; gap: 16px;
  }
  .brand-dot {
    width: 34px; height: 34px; border-radius: 50%;
    background: var(--orange);
  }
  .brand-name {
    font-family: 'Poppins', sans-serif; font-weight: 600;
    color: var(--orange); letter-spacing: 1px;
  }
  .back-brand .brand-name { font-size: 64px; line-height: 1; }
  .back-tagline {
    position: absolute; left: 0; right: 0; top: 215px;
    text-align: center;
    font-family: 'Cinzel', serif; font-weight: 400;
    color: var(--white);
    font-size: 30px; line-height: 1.2; letter-spacing: 1px;
  }
  .back-motto {
    position: absolute; left: 0; right: 0; top: 318px;
    text-align: center;
    font-family: 'Poppins', sans-serif; font-weight: 400;
    color: var(--orange);
    font-size: 15px; letter-spacing: 1.5px;
  }
  /* Front side */
  .card-front { background: var(--white); }
  .front-wave { position: absolute; inset: 0; }
  .front-brand {
    position: absolute; left: 64px; top: 120px;
    display: flex; align-items: center; gap: 12px;
  }
  .front-brand .brand-dot { width: 30px; height: 30px; }
  .front-brand .brand-name { font-size: 46px; line-height: 1; }
  .divider {
    position: absolute; left: 340px; top: 66px;
    width: 1px; height: 150px; background: var(--rule);
  }
  .contact {
    position: absolute; left: 370px; top: 52px;
    font-family: 'Poppins', sans-serif; color: var(--ink);
  }
  .contact-name { font-size: 26px; font-weight: 700; letter-spacing: 0.5px; line-height: 1.1; }
  .contact-role { font-size: 14px; font-weight: 500; color: var(--orange); margin-bottom: 4px; }
  .contact-address { font-size: 14px; line-height: 1.35; margin-bottom: 8px; }
  .contact-line {
    display: flex; align-items: center; gap: 10px;
    font-size: 14px; line-height: 1.6;
  }
  .contact-icon { width: 18px; height: 18px; flex: none; }
  .website {
    position: absolute; right: 36px; bottom: 24px;
    font-family: 'Poppins', sans-serif; font-size: 16px; font-weight: 500;
    color: var(--white); letter-spacing: 0.5px;
  }
</style>
</head>
<body>
<main class="canvas">

  <section class="card card-back" aria-label="Card back">
    <div class="back-brand">
      <span class="brand-dot"></span>
      <span class="brand-name">Vorin</span>
    </div>
    <p class="back-tagline">Asset Management<br>and Supply Chain</p>
    <p class="back-motto">Real Simple Solutions to Big Problems</p>
  </section>

  <section class="card card-front" aria-label="Card front">
    <svg class="front-wave" viewBox="0 0 700 400" preserveAspectRatio="none" aria-hidden="true">
      <path fill="var(--orange)" d="M0,352 C250,346 430,302 560,244 C620,216 665,184 700,164 L700,400 L0,400 Z"/>
      <path fill="var(--black)" d="M0,336 C250,330 425,286 555,226 C615,198 660,166 696,146 C664,170 622,206 562,234 C430,296 250,340 0,343 Z"/>
    </svg>

    <div class="front-brand">
      <span class="brand-dot"></span>
      <span class="brand-name">Vorin</span>
    </div>

    <div class="divider"></div>

    <div class="contact">
      <p class="contact-name">MILO R ANDERS</p>
      <p class="contact-role">CEO</p>
      <p class="contact-address">PO BOX 418, Harlow Lane<br>7th street Brenfield</p>
      <p class="contact-line">
        <svg class="contact-icon" viewBox="0 0 18 18" aria-hidden="true">
          <circle cx="9" cy="9" r="9" fill="var(--orange)"/>
          <path fill="var(--white)" d="M6.2 4.6l1.4 1.8-.8 1.1c.5 1.1 1.3 1.9 2.4 2.4l1.1-.8 1.8 1.4-.7 1.5c-3.3-.3-6.3-3.3-6.6-6.6z"/>
        </svg>
        (555) 018-2244
      </p>
      <p class="contact-line">
        <svg class="contact-icon" viewBox="0 0 18 18" aria-hidden="true">
          <circle cx="9" cy="9" r="9" fill="var(--orange)"/>
          <rect x="4.5" y="6" width="9" height="6.5" rx="0.8" fill="var(--white)"/>
          <path d="M4.8 6.4L9 9.6l4.2-3.2" fill="none" stroke="var(--orange)" stroke-width="1"/>
        </svg>
        info@vorinmail.com
      </p>
    </div>

    <p class="website">www.vorinweb.com</p>
  </section>

</main>
</body>
</html>
```